Lumaray Vellardo needs your help to create a new identity design

We are a basketball team based in Crescentino, Italy.
The official club colors are royal blue and white.
Basically we need a new letterhead and envelope design but not necessary a new logo, but if you want to suggest us a new one we are glad to evaluate it.
If you need any other info please contact us.

Target Market(s)

athletes, their families, other clubs, public institutions, companies

Industry/Entity Type

Club

Font styles to use
Other font styles liked:
• the font of our logo or something very similar

Colors
0592cd
ffffff

Requirements
Must have
• our logo, attached to this request; address and other club info such as email address, phone number, facebook page, VAT lot and tax code and obviously our official club colors royal blue and white
Nice to have
• a clear, simple and quite minimal design. A watermark
Should not have
• any other graphic or images such as hoops, ball or court

```html
<!DOCTYPE html>
<html lang="it">
<head>
<meta charset="utf-8">
<title>Lumaray Vellardo – Letterhead &amp; Envelope</title>
<link href="https://fonts.googleapis.com/css2?family=Saira+Condensed:wght@700&family=Open+Sans:wght@400;600&display=swap" rel="stylesheet">
<style>
  :root{
    --bg:#e9edf1;
    --paper:#f4f4f4;
    --navy:#1d3b66;
    --blue:#0592cd;
    --blue-deep:#1d6f9a;
    --flap:#2a6f97;
    --gray:#a9a9a9;
    --gray-light:#d3d3d3;
    --text:#555b63;
  }
  *{box-sizing:border-box;margin:0;padding:0}
  html,body{width:1200px;height:950px;overflow:hidden;background:var(--bg)}
  body{position:relative;font-family:"Open Sans",Arial,sans-serif}

  /* Letterhead */
  .letterhead{position:absolute;left:120px;top:30px;width:960px;height:430px;background:var(--paper);box-shadow:0 2px 8px rgba(0,0,0,.15);overflow:hidden}
  .top-bar{position:absolute;left:400px;right:0;top:22px;height:12px;background:var(--gray)}
  .top-bar-tail{position:absolute;left:230px;top:22px;width:160px;height:6px;background:var(--gray-light)}
  .club-name{position:absolute;right:40px;top:52px;font-family:"Saira Condensed",Arial Narrow,sans-serif;font-weight:700;font-size:30px;color:var(--navy);letter-spacing:.5px;text-transform:uppercase}
  .brand-mark{position:absolute;left:44px;top:92px;display:flex;align-items:center;gap:10px}
  .brand-mark .dot{width:20px;height:20px;border-radius:50%;background:var(--blue)}
  .brand-mark span{font-family:"Saira Condensed",Arial Narrow,sans-serif;font-weight:700;font-size:26px;color:var(--navy);text-transform:uppercase;line-height:1}
  .side-tab{position:absolute;left:0;top:150px;width:66px;height:14px;background:var(--blue)}
  .watermark{position:absolute;right:70px;top:160px;font-family:"Saira Condensed",Arial Narrow,sans-serif;font-weight:700;font-size:44px;color:var(--navy);opacity:.07;text-transform:uppercase}
  .footer-line{position:absolute;left:0;right:0;bottom:14px;height:8px;background:var(--blue-deep)}
  .footer-gray{position:absolute;left:0;width:400px;bottom:22px;height:8px;background:var(--gray-light)}
  .footer-blue{position:absolute;left:410px;width:190px;bottom:22px;height:8px;background:var(--blue)}
  .footer-gray2{position:absolute;left:610px;width:150px;bottom:22px;height:8px;background:var(--gray-light)}
  .contacts{position:absolute;left:22px;bottom:40px;display:flex;gap:14px;font-size:12.5px;color:var(--text);align-items:center}
  .contacts li{list-style:none;display:flex;align-items:center;gap:5px}
  .contacts svg{width:11px;height:11px}
  .web-tab{position:absolute;right:0;bottom:14px;width:190px;height:60px;background:linear-gradient(180deg,var(--blue),var(--blue-deep));color:#fff;font-weight:600;font-size:17px;display:flex;align-items:center;justify-content:center}

  /* Envelope */
  .envelope{position:absolute;left:120px;top:490px;width:960px;height:430px}
  .env-flap{position:absolute;left:0;top:0;width:960px;height:110px}
  .env-body{position:absolute;left:0;top:60px;width:960px;height:370px;background:var(--paper);box-shadow:0 2px 8px rgba(0,0,0,.15)}
  .env-fold{position:absolute;left:18px;right:18px;top:90px;bottom:0;border:1px solid #e2e2e2;border-bottom:none;border-radius:14px 14px 0 0}
  .env-mark{position:absolute;right:150px;top:250px;display:flex;align-items:center;gap:10px}
  .env-mark .dot{width:18px;height:18px;border-radius:50%;background:var(--blue)}
  .env-mark span{font-family:"Saira Condensed",Arial Narrow,sans-serif;font-weight:700;font-size:22px;color:var(--navy);text-transform:uppercase}
</style>
</head>
<body>
  <section class="letterhead">
    <div class="top-bar"></div>
    <div class="top-bar-tail"></div>
    <div class="club-name">Lumaray Vellardo</div>
    <div class="brand-mark"><div class="dot"></div><span>Lumaray<br>Vellardo</span></div>
    <div class="side-tab"></div>
    <div class="watermark">Lumaray Vellardo</div>
    <ul class="contacts">
      <li><svg viewBox="0 0 10 10"><circle cx="5" cy="5" r="4.5" fill="#1d3b66"/><circle cx="5" cy="4" r="1.5" fill="#fff"/></svg>Suite 0, 248 Sample Way, Vellardo Italy 0018</li>
      <li><svg viewBox="0 0 10 10"><circle cx="5" cy="5" r="4.5" fill="#1d3b66"/><rect x="3.5" y="2.5" width="3" height="5" rx=".6" fill="#fff"/></svg>(00) 0000 0000</li>
      <li><svg viewBox="0 0 10 10"><circle cx="5" cy="5" r="4.5" fill="#1d3b66"/><rect x="2.5" y="3.2" width="5" height="3.6" fill="#fff"/></svg>example@example.com</li>
      <li><svg viewBox="0 0 10 10"><circle cx="5" cy="5" r="4.5" fill="#1d3b66"/><circle cx="5" cy="5" r="1.6" fill="#fff"/></svg>@lumarayvellardo</li>
      <li><svg viewBox="0 0 10 10"><circle cx="5" cy="5" r="4.5" fill="#1d3b66"/><circle cx="5" cy="5" r="1.6" fill="#fff"/></svg>Vat</li>
    </ul>
    <div class="footer-gray"></div>
    <div class="footer-blue"></div>
    <div class="footer-gray2"></div>
    <div class="footer-line"></div>
    <div class="web-tab">www.lumarayvellardo.it</div>
  </section>

  <section class="envelope">
    <svg class="env-flap" viewBox="0 0 960 110" role="img" aria-label="Blue geometric pattern on the envelope flap">
      <path d="M0 110 L0 40 Q0 0 40 0 L920 0 Q960 0 960 40 L960 110 Z" fill="var(--flap)"/>
    </svg>
    <div class="env-body">
      <div class="env-fold"></div>
      <div class="env-mark"><div class="dot"></div><span>Lumaray Vellardo</span></div>
    </div>
  </section>
</body>
</html>
```